Design a Box for our Pickles. Full color, in and out.

We sell Pickles in a Jar, but they break, so we need a box to put 4 in a row and ship them without breaking them. Attached is all you need to design this box and if there are any questions please let me know.
Our company is 7owls.net, and you can see the jars if you look for "cornichons" important! We have different flavors, and the size and name of our pickles are different than average.

We want to see playfully fun and colorful yet on-brand designs. All documents are attached.

We are looking for a full-color design inside and outside. To protect our pickles. If there are any questions, feel free to ask.

HERE ARE REFERENCES OF WHAT WE WANT: something more playful, not something that looks exactly like one of our product packaging.

https://artboardhub.example/profiles/marisolda/designs/5283610
https://artboardhub.example/profiles/8031926/designs/6690273
https://artboardhub.example/profiles/tolvik/designs/3058841

Target Market(s)

Young people, fancy, fun.

Industry/Entity Type

Retail food and perpuses

Font styles to use
Other font styles liked:
• Attached!

Requirements
Must have
• Must look beutifull and simple, not with too many elements, and must be on brand! Please look at the brand book!
Nice to have
• Clever quotes, fun to see.
Should not have
• must not look exactly like our packaging

```html
<!DOCTYPE html>
<html lang="en">
<head>
<meta charset="utf-8">
<title>Seven Owls — Cornichons Piquants shipping box</title>
<link rel="stylesheet" href="https://fonts.googleapis.com/css2?family=Oswald:wght@500;600;700&family=Source+Sans+3:wght@400;600&family=Caveat:wght@500&display=swap">
<style>
  :root {
    --backdrop: #e4e4e4;
    --box-red: #972a37;
    --box-red-deep: #85202d;
    --cream: #ebe6da;
    --cream-edge: #ddd6c6;
    --white: #ffffff;
    --accent-orange: #e0875c;
    --stamp-red: #a33442;
    --seal-green: #2e8a57;
    --seal-brown: #7a4a2a;
    --ink: #2a1a1c;
  }
  * { box-sizing: border-box; margin: 0; padding: 0; }
  html, body { width: 1200px; height: 800px; overflow: hidden; }
  body { background: var(--backdrop); font-family: "Source Sans 3", sans-serif; position: relative; }

  .dieline { position: absolute; left: 60px; top: 140px; width: 1080px; height: 520px; }
  .panel { position: absolute; }
  .panel--top {
    left: 220px; top: 0; width: 640px; height: 200px;
    background: var(--box-red); border-bottom: 1px dashed rgba(255,255,255,.25);
    display: flex; align-items: center; justify-content: center;
  }
  .panel--front { left: 220px; top: 200px; width: 640px; height: 320px; background: var(--box-red); }
  .panel--end-left, .panel--end-right {
    top: 200px; width: 220px; height: 320px; background: var(--cream);
  }
  .panel--end-left { left: 0; border-right: 1px dashed var(--cream-edge); }
  .panel--end-right { left: 860px; border-left: 1px dashed var(--cream-edge); }

  /* brand lockups */
  .brand-mark { border: 2px solid var(--white); border-radius: 50%; flex: none; }
  .top-lockup { display: flex; align-items: center; gap: 12px; }
  .top-lockup .brand-mark { width: 44px; height: 44px; }
  .brand-name {
    font-family: "Oswald", sans-serif; font-weight: 600; color: var(--white);
    letter-spacing: .08em; text-transform: uppercase;
  }
  .top-lockup .brand-name { font-size: 18px; }

  .front-lockup {
    position: absolute; left: 150px; top: 70px; display: flex; align-items: center; gap: 18px;
  }
  .front-lockup .brand-mark { width: 110px; height: 110px; }
  .product-title { color: var(--white); font-family: "Oswald", sans-serif; text-transform: uppercase; line-height: .95; }
  .product-title .brand-name { display: block; font-size: 14px; margin-bottom: 6px; }
  .product-title .line-one { display: block; font-size: 30px; font-weight: 600; }
  .product-title .line-two { display: block; font-size: 52px; font-weight: 700; }

  .recipe-note {
    position: absolute; right: 140px; bottom: 70px; text-align: center;
    font-family: "Caveat", cursive; color: var(--accent-orange); font-size: 22px; line-height: 1.1;
  }
  .recipe-note .rule { display: block; width: 90px; height: 1px; background: var(--accent-orange); margin: 3px auto; }

  .count-tag {
    position: absolute; right: 30px; bottom: 64px; width: 90px; height: 62px;
    border: 1.5px solid var(--white); color: var(--white); text-align: center;
  }
  .count-tag .count { display: block; font-family: "Oswald", sans-serif; font-weight: 700; font-size: 24px; margin-top: 6px; line-height: 1; }
  .count-tag .label { display: block; font-size: 10px; letter-spacing: .45em; margin-top: 4px; }

  .fine-print {
    position: absolute; left: 40px; bottom: 26px; width: 300px;
    color: var(--white); font-size: 8.5px; line-height: 1.35;
  }
  .panel--end-right .fine-print { color: var(--ink); left: 25px; width: 170px; text-align: center; }

  /* claim stamps */
  .claims { display: flex; flex-direction: column; align-items: center; padding-top: 36px; gap: 10px; }
  .claim-stamp {
    width: 76px; height: 76px; border-radius: 50%; border: 2px solid var(--stamp-red);
    color: var(--stamp-red); font-family: "Oswald", sans-serif; font-weight: 500;
    font-size: 10px; line-height: 1.1; text-align: center; text-transform: uppercase;
    display: flex; flex-direction: column; justify-content: center;
  }
  .claim-stamp .big { font-size: 16px; font-weight: 600; }
  .claim-divider { width: 6px; height: 3px; background: var(--stamp-red); }
  .cert-seal { width: 76px; height: 76px; border-radius: 50%; background: var(--seal-green); border: 4px solid var(--seal-brown); }

  /* award */
  .award { position: absolute; left: 30px; top: 60px; width: 160px; height: 130px; }
  .award .laurel { position: absolute; top: 0; width: 28px; height: 130px; border-radius: 50%; background: var(--accent-orange); opacity: .35; }
  .award .laurel--left { left: 0; }
  .award .laurel--right { right: 0; }
  .award-text {
    position: absolute; left: 32px; right: 32px; top: 16px; text-align: center;
    font-family: "Oswald", sans-serif; color: var(--accent-orange); text-transform: uppercase; line-height: 1;
  }
  .award-text .brand-name { color: var(--accent-orange); font-size: 12px; display: block; }
  .award-count { display: inline-block; font-size: 48px; font-weight: 700; vertical-align: middle; }
  .award-label { display: inline-block; font-size: 11px; font-weight: 500; text-align: left; vertical-align: middle; }
</style>
</head>
<body>
  <main class="dieline">
    <section class="panel panel--top">
      <div class="top-lockup">
        <span class="brand-mark"></span>
        <span class="brand-name">Seven Owls</span>
      </div>
    </section>

    <section class="panel panel--end-left">
      <div class="claims">
        <div class="claim-stamp"><span class="big">No</span><span>Antibiotics</span><span>Ever</span></div>
        <span class="claim-divider"></span>
        <div class="claim-stamp"><span class="big">No</span><span>Nitrites or</span><span>Nitrates</span><span>Added</span></div>
        <span class="claim-divider"></span>
        <div class="cert-seal" role="img" aria-label="Organic certification seal"></div>
      </div>
    </section>

    <section class="panel panel--front">
      <div class="front-lockup">
        <span class="brand-mark"></span>
        <h1 class="product-title">
          <span class="brand-name">Seven Owls</span>
          <span class="line-one">Cornichons</span>
          <span class="line-two">Piquants</span>
        </h1>
      </div>
      <p class="fine-print">Lorem ipsum dolor sit amet, consectetur adipiscing elit, idunt ut lab dolore magna aliqua. Convallis tellus id interdum olutpat ac tincidunt vitae semper. Nisi nisi scelerisque eu ultrices vm dignissim diam quis.</p>
      <p class="recipe-note">French Recipe<span class="rule"></span>Since 1975</p>
      <div class="count-tag"><span class="count">4 JARS</span><span class="label">INSIDE</span></div>
    </section>

    <section class="panel panel--end-right">
      <div class="award">
        <span class="laurel laurel--left" role="img" aria-label="Laurel wreath, left branch"></span>
        <span class="laurel laurel--right" role="img" aria-label="Laurel wreath, right branch"></span>
        <div class="award-text">
          <span class="brand-name">Seven Owls</span>
          <span class="award-count">21</span>
          <span class="award-label">National<br>Food<br>Awards</span>
        </div>
      </div>
      <p class="fine-print" style="bottom:90px">Lorem ipsum dolor sit amet, adipiscing elit, idunt ut lab dolore magna aliqua. Convallis tellus id olutpat ac tincidunt vitae semper. Nisi nisi scelerisque vm dignissim diam quis.</p>
    </section>
  </main>
</body>
</html>
```